New modern business card design

To design a brand new business card that's clean & modern in terms of layout.
I have attached our company logo and also basic information regarding what is needed on the card that also needs to be editable.

Target Market(s)

motor trade

Contact Information for Business Card

logo, name, title, tel, mob, email, address, www, all information is in the word.doc file

Requirements
Must have
• white background
Nice to have
• Nice clean font

```html
<!DOCTYPE html>
<html lang="en">
<head>
<meta charset="utf-8">
<title>Kessock Fixings Ltd – Business Card</title>
<link rel="stylesheet" href="https://fonts.googleapis.com/css2?family=Lato:wght@400;700&family=Michroma&display=swap">
<style>
  :root {
    --cyan: #38c8fb;
    --white: #ffffff;
    --panel-light: #5e5e5e;
    --panel-dark: #343434;
    --ink: #ffffff;
  }
  html, body {
    margin: 0;
    padding: 0;
    width: 1200px;
    height: 686px;
    overflow: hidden;
    background: var(--white);
  }
  .card {
    position: relative;
    width: 1200px;
    height: 686px;
    background: var(--white);
    overflow: hidden;
  }
  .card-shapes {
    position: absolute;
    inset: 0;
  }
  .person-name {
    position: absolute;
    left: 75px;
    top: 78px;
    margin: 0;
    font-family: "Michroma", sans-serif;
    font-weight: 400;
    font-size: 36px;
    letter-spacing: 1px;
    color: var(--ink);
    white-space: nowrap;
  }
  .person-title {
    position: absolute;
    left: 120px;
    top: 138px;
    margin: 0;
    font-family: "Lato", sans-serif;
    font-weight: 400;
    font-size: 25px;
    letter-spacing: 11px;
    color: var(--ink);
    white-space: nowrap;
  }
  .company-mark {
    position: absolute;
    left: 60px;
    top: 315px;
    width: 450px;
    text-align: center;
  }
  .company-mark .mark-square {
    display: block;
    width: 60px;
    height: 60px;
    margin: 0 auto 26px;
    background: var(--cyan);
  }
  .company-mark .company-name {
    margin: 0;
    font-family: "Michroma", sans-serif;
    font-weight: 400;
    font-size: 26px;
    line-height: 1.5;
    letter-spacing: 1px;
    color: var(--cyan);
  }
  .contact-text {
    position: absolute;
    margin: 0;
    font-family: "Lato", sans-serif;
    font-weight: 700;
    font-size: 21px;
    line-height: 32px;
    color: var(--ink);
    text-align: center;
    white-space: nowrap;
  }
  .contact-address { left: 780px; width: 400px; top: 250px; }
  .contact-phone   { left: 800px; width: 270px; top: 390px; }
  .contact-web     { left: 810px; width: 390px; top: 534px; }
</style>
</head>
<body>
<div class="card">
  <svg class="card-shapes" width="1200" height="686" viewBox="0 0 1200 686" aria-hidden="true">
    <defs>
      <radialGradient id="panelShade" cx="0.5" cy="0.4" r="0.75">
        <stop offset="0" stop-color="var(--panel-light)"/>
        <stop offset="1" stop-color="var(--panel-dark)"/>
      </radialGradient>
    </defs>
    <!-- edge bands -->
    <rect class="band-top" x="0" y="0" width="1200" height="20" fill="var(--cyan)"/>
    <rect class="band-bottom" x="0" y="662" width="1200" height="24" fill="var(--cyan)"/>

    <!-- name header -->
    <polygon class="header-panel" points="0,34 709,34 737,198 0,198" fill="url(#panelShade)"/>

    <!-- address row -->
    <polygon class="icon-tile" points="600,215 737,215 763,351 626,351" fill="var(--cyan)"/>
    <polygon class="info-panel" points="748,215 1200,215 1200,351 774,351" fill="url(#panelShade)"/>
    <!-- phone row -->
    <polygon class="icon-tile" points="628,362 765,362 791,498 654,498" fill="var(--cyan)"/>
    <polygon class="info-panel" points="776,362 1200,362 1200,498 802,498" fill="url(#panelShade)"/>
    <!-- web row -->
    <polygon class="icon-tile" points="656,510 793,510 819,646 682,646" fill="var(--cyan)"/>
    <polygon class="info-panel" points="804,510 1200,510 1200,646 830,646" fill="url(#panelShade)"/>

    <!-- pin icon -->
    <g class="icon-pin" transform="translate(682,283)">
      <path d="M0,40 C-12,24 -28,10 -28,-8 A28,28 0 0 1 28,-8 C28,10 12,24 0,40 Z" fill="var(--white)"/>
      <circle cx="0" cy="-8" r="15" fill="var(--cyan)"/>
      <circle cx="0" cy="-8" r="9" fill="var(--white)"/>
    </g>

    <!-- contact silhouette icon -->
    <g class="icon-contact" transform="translate(709,430)">
      <ellipse cx="0" cy="-16" rx="17" ry="21" fill="var(--white)"/>
      <path d="M-37,36 C-37,14 -22,6 -8,4 L8,4 C22,6 37,14 37,36 Z" fill="var(--white)"/>
    </g>

    <!-- globe icon -->
    <g class="icon-globe" transform="translate(736,578)" fill="none" stroke="var(--white)" stroke-width="5">
      <circle cx="0" cy="0" r="32"/>
      <ellipse cx="0" cy="0" rx="13" ry="32"/>
      <line x1="0" y1="-32" x2="0" y2="32"/>
      <line x1="-32" y1="0" x2="32" y2="0"/>
      <path d="M-27,-16 H27 M-27,16 H27"/>
    </g>
  </svg>

  <h1 class="person-name">DARREN WHITLOW</h1>
  <p class="person-title">General Manager</p>

  <div class="company-mark">
    <span class="mark-square"></span>
    <p class="company-name">KESSOCK FIXINGS<br>LTD</p>
  </div>

  <p class="contact-text contact-address">Mill Lane / Droylsden,<br>Manchester / M43 7QP</p>
  <p class="contact-text contact-phone">07700 900 418<br>0161 496 0725</p>
  <p class="contact-text contact-web">dwhitlow@kessock-fixings.co.uk<br>www.kessock-fixings.co.uk</p>
</div>
</body>
</html>
```